Eye catching business card using our brand new logo
Dorvik Fabrication, Inc.
Modern
Wendell R. Fostrey
President
58 Quarry Hollow Road
Brindle, NH 03419
WFostrey@norvax.net
We would like to see many different styles of our brand new logo used in our business cards. Some would fill the card with the logo and some using it in the lower left corner of the card

```html
<!DOCTYPE html>
<html lang="en">
<head>
<meta charset="utf-8">
<title>Dorvik Fabrication, Inc. — Business Card</title>
<link rel="stylesheet" href="https://fonts.googleapis.com/css2?family=Open+Sans:wght@400;600;700&display=swap">
<style>
  :root{
    --stage:#e9eaec;
    --card:#ffffff;
    --card-shade:#eef0f2;
    --brand-blue:#2f49c4;
    --brand-blue-dark:#233a9e;
    --swoosh-grey:#9ea3aa;
    --ink:#3b3f45;
    --ink-soft:#7a7f86;
    --on-blue:#ffffff;
  }
  *{box-sizing:border-box;margin:0;padding:0}
  html,body{width:1200px;height:864px;overflow:hidden}
  body{
    background:var(--stage);
    font-family:"Open Sans",Arial,sans-serif;
    position:relative;
  }
  .card{
    position:absolute;
    top:277px;
    width:540px;
    height:310px;
    border-radius:26px;
    background:linear-gradient(180deg,var(--card) 0%,var(--card-shade) 100%);
    box-shadow:0 6px 18px rgba(0,0,0,.12);
    overflow:hidden;
  }
  .card--front{left:40px}
  .card--back{left:620px}

  /* front */
  .brand-mark{
    position:absolute;
    left:0;right:0;top:104px;
    display:flex;align-items:center;justify-content:center;gap:12px;
  }
  .brand-mark__dot{
    width:26px;height:26px;border-radius:50%;
    background:var(--brand-blue);
  }
  .brand-mark__name{
    font-size:24px;font-weight:700;color:var(--ink);
  }
  .website{
    position:absolute;left:0;right:0;bottom:46px;
    text-align:center;
    font-size:15px;letter-spacing:6px;color:var(--ink);
  }

  /* back */
  .back-art{position:absolute;inset:0}
  .back-logo{
    position:absolute;left:30px;top:150px;
    display:flex;align-items:center;gap:8px;
  }
  .back-logo__dot{
    width:18px;height:18px;border-radius:50%;
    background:var(--brand-blue);
  }
  .back-logo__name{
    font-size:15px;font-weight:700;color:var(--brand-blue);
  }
  .person{position:absolute;left:30px;bottom:34px}
  .person__name{font-size:15px;font-weight:700;color:var(--brand-blue)}
  .person__title{font-size:12px;color:var(--ink-soft);margin-top:2px}

  .contact{
    position:absolute;right:28px;top:70px;
    list-style:none;
    display:flex;flex-direction:column;gap:9px;
  }
  .contact__item{
    display:flex;align-items:flex-start;gap:8px;
    color:var(--on-blue);font-size:11.5px;line-height:1.35;
  }
  .contact__icon{
    flex:0 0 16px;width:16px;height:16px;
    border-radius:50%;background:var(--on-blue);
    display:flex;align-items:center;justify-content:center;
  }
  .contact__icon svg{width:10px;height:10px}
</style>
</head>
<body>

<section class="card card--front" aria-label="Business card front">
  <div class="brand-mark">
    <span class="brand-mark__dot"></span>
    <span class="brand-mark__name">Dorvik Fabrication, Inc.</span>
  </div>
  <p class="website">www.dorvikfab.com</p>
</section>

<section class="card card--back" aria-label="Business card back">
  <svg class="back-art" viewBox="0 0 540 310" preserveAspectRatio="none" aria-hidden="true">
    <path d="M280 0 C 350 90, 350 220, 250 310 L 540 310 L 540 0 Z" fill="var(--swoosh-grey)"/>
    <path d="M300 0 C 372 90, 372 220, 272 310 L 540 310 L 540 0 Z" fill="var(--brand-blue)"/>
    <path d="M300 0 C 372 90, 372 220, 272 310" fill="none" stroke="var(--brand-blue-dark)" stroke-width="3"/>
  </svg>

  <ul class="contact">
    <li class="contact__item">
      <span class="contact__icon"><svg viewBox="0 0 10 10"><path d="M5 0.5a3 3 0 0 0-3 3c0 2.3 3 6 3 6s3-3.7 3-6a3 3 0 0 0-3-3zm0 4.2a1.2 1.2 0 1 1 0-2.4 1.2 1.2 0 0 1 0 2.4z" fill="var(--brand-blue)"/></svg></span>
      <span>58 Quarry Hollow Road<br>Brindle, NH 03419</span>
    </li>
    <li class="contact__item">
      <span class="contact__icon"><svg viewBox="0 0 10 10"><path d="M2.3 1l1.5 1.8-.8 1.1a5.5 5.5 0 0 0 2.9 2.9l1.1-.8L8.8 7.5 7.9 8.9C4.5 8.9 1.1 5.5 1.1 2.1z" fill="var(--brand-blue)"/></svg></span>
      <span>(603) 555-0148</span>
    </li>
    <li class="contact__item">
      <span class="contact__icon"><svg viewBox="0 0 10 10"><path d="M2.3 1l1.5 1.8-.8 1.1a5.5 5.5 0 0 0 2.9 2.9l1.1-.8L8.8 7.5 7.9 8.9C4.5 8.9 1.1 5.5 1.1 2.1z" fill="var(--brand-blue)"/></svg></span>
      <span>(603) 555-0192</span>
    </li>
    <li class="contact__item">
      <span class="contact__icon"><svg viewBox="0 0 10 10"><rect x="1" y="2.5" width="8" height="5.5" rx=".6" fill="var(--brand-blue)"/><path d="M1.4 3l3.6 2.6L8.6 3" fill="none" stroke="#fff" stroke-width=".8"/></svg></span>
      <span>WFostrey@norvax.net</span>
    </li>
  </ul>

  <div class="back-logo">
    <span class="back-logo__dot"></span>
    <span class="back-logo__name">Dorvik Fabrication, Inc.</span>
  </div>

  <div class="person">
    <p class="person__name">Wendell R. Fostrey</p>
    <p class="person__title">President</p>
  </div>
</section>

</body>
</html>
```